Wine Can for New StartUp Winery (Silver Heron Sangría)

Hello everyone! After years of crafting the perfect sangría, we’re thrilled to launch it in a can for the first time. We’re looking to create a premium, elegant design that reflects the high quality and deliciousness of our beloved drink. Can you help us design the can everyone will love?

We encourage your creativity, so have fun with it! There are just a few guidelines:

NAME: SILVER HERON SANGRÍA
LOGO: Bull
PRODUCT: Wine, Sangría Española
COLOR: Primary colors are red and white
DIMENSIONS: 250ml can
STYLE: Elegant, modern, sophisticated, misty
INFORMATION: Live space for the ingredients, % alcohol, country
CAN MATERIAL: The material is alumium (ensure that the print will match the colors)
KEEP IN MIND: Premium

Places to help you with some ideas:
Web Page: https://www.lunadelsurfoods.com.au/sangria/
Instagram: https://www.instagram.com/silverheronsangria/

Target Market(s)

Wine lovers

Industry/Entity Type

Winery

Colors
EB3D1F
EC4F4E
F09395
F8D3D4
FCEDEE

Requirements
Must have
• The logo, the signature of Tobías, the bull
Nice to have
• Big bull, wine motion liquid, misty effect as cold
Should not have
• So many icons or figures

```html
<!DOCTYPE html>
<html lang="en">
<head>
<meta charset="utf-8">
<title>Silver Heron Sangría – Can Label</title>
<link rel="stylesheet" href="https://fonts.googleapis.com/css2?family=Poppins:wght@400;500;700&display=swap">
<style>
  :root {
    --page: #f7f9fc;
    --white: #ffffff;
    --stripe-red: #e2252f;
    --field-top: #e03d27;
    --field-mid: #cf4430;
    --field-bottom: #c23a30;
    --panel-top: #d9232f;
    --panel-bottom: #b82a31;
  }
  * { box-sizing: border-box; margin: 0; padding: 0; }
  html, body { width: 707px; height: 1200px; overflow: hidden; }
  body {
    background: var(--page);
    font-family: "Poppins", sans-serif;
    color: var(--white);
    position: relative;
  }
  .can-label {
    position: absolute;
    left: 42px;
    top: 360px;
    width: 623px;
    height: 479px;
  }
  .stripe { position: absolute; left: 0; width: 100%; background: var(--stripe-red); }
  .stripe--top-wide { top: 0; height: 7px; }
  .stripe--top-thin { top: 10px; height: 4px; }
  .stripe--bottom-thin { top: 468px; height: 4px; }
  .stripe--bottom-wide { top: 475px; height: 4px; }
  .label-field {
    position: absolute;
    left: 0; top: 21px;
    width: 100%; height: 441px;
    background: linear-gradient(170deg, var(--field-top) 0%, var(--field-mid) 50%, var(--field-bottom) 100%);
    overflow: hidden;
  }
  .brand-mark {
    position: absolute;
    left: 178px; top: 65px;
    width: 60px; height: 60px;
    border-radius: 50%;
    background: var(--white);
  }
  .brand-name {
    position: absolute;
    left: 0; top: 150px;
    width: 416px;
    text-align: center;
    font-weight: 700;
    font-size: 20px;
    line-height: 22px;
    letter-spacing: 0.2px;
  }
  .product-name {
    position: absolute;
    left: 112px; top: 291px;
    width: 192px;
    text-align: center;
    font-weight: 400;
    font-size: 20px;
    line-height: 26px;
    letter-spacing: 0.4px;
    padding-bottom: 7px;
    border-bottom: 2px solid var(--white);
  }
  .volume-tab {
    position: absolute;
    left: 169px; top: 374px;
    width: 79px; height: 70px;
    border: 1.5px solid var(--white);
    border-bottom: none;
    border-radius: 5px 5px 0 0;
    padding: 2px 2px 0;
  }
  .volume-tab__inner {
    height: 100%;
    border: 1.5px solid var(--white);
    border-bottom: none;
    border-radius: 4px 4px 0 0;
    text-align: center;
    font-size: 14px;
    letter-spacing: -0.3px;
  }
  .volume-tab__size { padding-top: 6px; line-height: 20px; }
  .volume-tab__rule { width: 61px; height: 1.5px; background: var(--white); margin: 2px auto 6px; }
  .volume-tab__alc { line-height: 20px; }
  .ingredients-panel {
    position: absolute;
    left: 440px; top: 60px;
    width: 158px; height: 342px;
    border: 2px solid var(--white);
    background: linear-gradient(180deg, var(--panel-top), var(--panel-bottom));
    text-align: center;
  }
  .ingredients-panel__title {
    margin-top: 6px;
    font-weight: 500;
    font-size: 17.5px;
    letter-spacing: 0.3px;
  }
</style>
</head>
<body>
  <section class="can-label">
    <div class="stripe stripe--top-wide"></div>
    <div class="stripe stripe--top-thin"></div>

    <div class="label-field" role="img" aria-label="Marbled red and orange wine-in-motion liquid pattern">
      <div class="brand-mark"></div>
      <h1 class="brand-name">SILVER HERON<br>SANGRÍA</h1>
      <p class="product-name">Sangría Española</p>
      <div class="volume-tab">
        <div class="volume-tab__inner">
          <div class="volume-tab__size">250 ml</div>
          <div class="volume-tab__rule"></div>
          <div class="volume-tab__alc">ALC 20%</div>
        </div>
      </div>
      <div class="ingredients-panel">
        <h2 class="ingredients-panel__title">INGREDIENTS</h2>
      </div>
    </div>

    <div class="stripe stripe--bottom-thin"></div>
    <div class="stripe stripe--bottom-wide"></div>
  </section>
</body>
</html>
```